Collagen Tub Packaging Design for a New Brand

PLEASE DON'T SEND ANY NEW DESIGNS WE JUST HAVE TO DECIDE WITH MY PARTNERS THANKS A LOT.
I've created a very detailed document & design examples of what we like in certain designs and what we don't.

There are 3 documents:
1- Brief for the Design (please read it before designing)
2- Brand Design Examples that we like (and why we like them)
3- Die cut for the packaging design. This will be it's dimensions.

We are NOT looking for someone to micro-manage. In contrast, we want someone to help us express our ideas better with their design. Nothing I say in these briefs are there to limit the creativity of the designer, because if we knew exactly what we wanted we would do it ourselves but we trust the designer's expertise in this packaging design.

In short: We want our brand to feel premium, high-quality & trust worthy with it's design not feeling very busy or bloated. We don't have a logo source file, but you'll get the idea of what we want when you see it).

Let me know if you have any further questions, will answer each question real fast.

Thanks.

Target Market(s)

Pretty much everyone above 25+ in Turkey because nearly all of them are using are collagens so our audience is wild.

Industry/Entity Type

Collagen - Health, Wellness & Supplements

Font styles to use
Serif
Sans Serif

Colors

Designer to choose colors to be used in the design.

Requirements
Must have
• Our design should be distinct, a design style which everyone can identify from 10 meters away if they know the product. This is a MUST have for us. It's up to designer to achieve it. This can be just a simple color palette aswell.
Should not have
• It shouldn't feel bloated and very busy. Please avoid very detailed icons (as a rule of thumb, if you can make it work great)

```html
<!DOCTYPE html>
<html lang="en">
<head>
<meta charset="UTF-8">
<title>Solvera Hydrolized Collagen Label</title>
<link href="https://fonts.googleapis.com/css2?family=Fraunces:opsz,wght@9..144,800;9..144,900&family=Montserrat:wght@500;600;700&family=Oswald:wght@500;600&display=swap" rel="stylesheet">
<style>
  :root {
    --brand-blue: #3552c0;
    --brand-blue-deep: #2741a8;
    --band-light: #4a6ad0;
    --label-white: #ffffff;
    --text-grey: #5a5f6b;
    --rule-grey: #e1e3e8;
    --arch-edge: #d9dce4;
  }
  * { margin: 0; padding: 0; box-sizing: border-box; }
  html, body {
    width: 1166px; height: 1200px; overflow: hidden;
    background: var(--label-white);
  }
  .label {
    position: relative; width: 1166px; height: 1200px;
    background: var(--label-white);
    font-family: 'Montserrat', sans-serif;
    color: var(--brand-blue);
  }
  .top-band { position: absolute; left: 0; top: 0; width: 1166px; height: 300px; display: block; }
  .brand {
    position: absolute; left: 0; right: 0; top: 125px; text-align: center;
  }
  .brand-name {
    font-family: 'Montserrat', sans-serif; font-weight: 600;
    font-size: 96px; line-height: 1; color: var(--brand-blue);
    letter-spacing: 1px;
  }
  .headline { position: absolute; left: 0; right: 0; top: 0; height: 700px; font-weight: normal; }
  .headline-top {
    position: absolute; left: 549px; top: 312px;
    font-family: 'Fraunces', serif; font-weight: 800; font-size: 78px; line-height: 1;
  }
  .headline-main {
    position: absolute; left: 0; right: 0; top: 400px; text-align: center;
    font-family: 'Fraunces', serif; font-weight: 900; font-size: 190px; line-height: 1;
    letter-spacing: -3px;
  }
  .headline-bottom {
    position: absolute; left: 205px; top: 568px;
    font-family: 'Fraunces', serif; font-weight: 800; font-size: 80px; line-height: 1;
  }
  .collagen-types {
    position: absolute; left: 0; right: 0; top: 692px; text-align: center;
    font-weight: 600; font-size: 45px; letter-spacing: 1px;
  }
  .dose-pill {
    position: absolute; left: 50%; top: 764px; transform: translateX(-50%);
    background: var(--brand-blue-deep); color: var(--label-white);
    font-weight: 600; font-size: 34px; letter-spacing: 1px;
    padding: 10px 50px; border-radius: 40px; white-space: nowrap;
  }
  .benefits {
    position: absolute; left: 242px; top: 886px; list-style: none;
  }
  .benefits li {
    font-weight: 500; font-size: 21px; letter-spacing: 1.5px; color: var(--text-grey);
    line-height: 1; margin-bottom: 35px; position: relative; padding-left: 55px;
  }
  .benefits li::before {
    content: "+"; position: absolute; left: 0; top: -5px;
    color: var(--brand-blue); font-weight: 700; font-size: 28px;
  }
  .stats-rule {
    position: absolute; left: 133px; right: 141px; top: 1048px;
    height: 2px; background: var(--rule-grey);
  }
  .stats {
    position: absolute; left: 150px; right: 150px; top: 1078px;
    display: flex; justify-content: space-between;
  }
  .stat { text-align: center; min-width: 130px; }
  .stat-value {
    font-family: 'Oswald', sans-serif; font-weight: 600; font-size: 58px; line-height: 1;
    color: var(--brand-blue);
  }
  .stat-label {
    font-family: 'Oswald', sans-serif; font-weight: 500; font-size: 24px; letter-spacing: 1px;
    color: var(--text-grey); margin-top: 8px;
  }
</style>
</head>
<body>
  <main class="label">
    <svg class="top-band" viewBox="0 0 1166 300" aria-hidden="true">
      <defs>
        <linearGradient id="bandGradient" x1="0" y1="0" x2="1" y2="0">
          <stop offset="0" stop-color="var(--band-light)"/>
          <stop offset="0.5" stop-color="var(--brand-blue)"/>
          <stop offset="1" stop-color="var(--brand-blue-deep)"/>
        </linearGradient>
      </defs>
      <rect x="0" y="0" width="1166" height="281" fill="url(#bandGradient)"/>
      <path d="M0 300 L0 281 L164 281 C240 90 360 45 583 45 C806 45 926 90 1002 281 L1166 281 L1166 300 Z" fill="var(--label-white)"/>
      <path d="M164 281 C240 90 360 45 583 45 C806 45 926 90 1002 281" fill="none" stroke="var(--arch-edge)" stroke-width="4"/>
    </svg>

    <header class="brand">
      <div class="brand-name">Solvera</div>
    </header>

    <h1 class="headline">
      <span class="headline-top">hidrolized</span>
      <span class="headline-main">collagen</span>
      <span class="headline-bottom">peptides</span>
    </h1>

    <p class="collagen-types">TYPE 1 &amp; TYPE 2 COLLAGEN</p>
    <p class="dose-pill">100 MG PER SCOOP</p>

    <ul class="benefits">
      <li>NATURAL VITAMIN C FROM ACEROLA</li>
      <li>SILISIUM FOR ENHANCED ABSORPTION</li>
      <li>PROBIOTICS FOR OVERALL HEALTH &amp; GUT HEALTH</li>
    </ul>

    <div class="stats-rule"></div>
    <section class="stats">
      <div class="stat"><div class="stat-value">0g</div><div class="stat-label">CARB</div></div>
      <div class="stat"><div class="stat-value">0g</div><div class="stat-label">FAT</div></div>
      <div class="stat"><div class="stat-value">0g</div><div class="stat-label">SUGAR</div></div>
      <div class="stat"><div class="stat-value">11g</div><div class="stat-label">PROTEIN</div></div>
      <div class="stat"><div class="stat-value">12g</div><div class="stat-label">COLLAGEN</div></div>
    </section>
  </main>
</body>
</html>
```